Business Card Design

Kitchen Cabinet company in Colorado. We recently changed our logo the use the colors grey and blue. Our company motto is "crafted for the way you live" Wanting a business card to pop and stand out. I attached our new logo and colors scheme

Industry/Entity Type

Business

```html
<!DOCTYPE html>
<html lang="en">
<head>
<meta charset="UTF-8">
<title>Aspenwood Kitchens – Business Card</title>
<link rel="stylesheet" href="https://fonts.googleapis.com/css2?family=Open+Sans:ital,wght@0,300;1,300&display=swap">
<style>
  :root {
    --paper: #ffffff;
    --card-slate: #3e5666;
    --ink-light: #ffffff;
  }
  html, body {
    margin: 0;
    padding: 0;
    width: 1200px;
    height: 702px;
    overflow: hidden;
    background: var(--paper);
  }
  .card {
    position: absolute;
    left: 22px;
    top: 22px;
    width: 1155px;
    height: 657px;
    background: var(--card-slate);
    color: var(--ink-light);
    font-family: "Open Sans", sans-serif;
    font-weight: 300;
  }
  .identity {
    position: absolute;
    left: 111px;
    top: 84px;
    margin: 0;
    font-size: 40px;
    line-height: 44px;
    font-weight: 300;
  }
  .identity span { display: block; }
  .contact {
    position: absolute;
    left: 111px;
    font-style: italic;
    font-size: 23px;
    line-height: 27.5px;
    letter-spacing: 0.2px;
    margin: 0;
  }
  .contact span { display: block; }
  .contact--address { top: 224px; }
  .contact--lines { top: 300px; }
  .divider {
    position: absolute;
    left: 623px;
    top: 223px;
    width: 8px;
    height: 210px;
    background: var(--ink-light);
  }
  .brand {
    position: absolute;
    left: 650px;
    top: 262px;
    width: 478px;
    text-align: center;
  }
  .brand-name {
    margin: 0;
    font-size: 50px;
    line-height: 56px;
    font-weight: 300;
    letter-spacing: 3px;
    text-transform: uppercase;
  }
  .brand-motto {
    margin: 12px 0 0;
    font-size: 29px;
    line-height: 34px;
    font-weight: 300;
    letter-spacing: 0.3px;
  }
</style>
</head>
<body>
  <main class="card">
    <h1 class="identity">
      <span class="identity-name">Jordan Hale</span>
      <span class="identity-role">Designer/Sales</span>
    </h1>

    <address class="contact contact--address">
      <span>2480 Ridgeview Lane</span>
      <span>Pinecrest, CO 80421</span>
    </address>

    <p class="contact contact--lines">
      <span>ph.555.210.4837</span>
      <span>cell.555.318.6294</span>
      <span>fax.555.642.0915</span>
      <span>email jhale@aspenwoodkitchens.com</span>
      <span>website. www.aspenwoodkitchens.com</span>
    </p>

    <div class="divider" aria-hidden="true"></div>

    <div class="brand">
      <p class="brand-name">Aspenwood<br>Kitchens</p>
      <p class="brand-motto">crafted for the way you live</p>
    </div>
  </main>
</body>
</html>
```